Add words, element to an already make product design

Hi guys,
I m already have the design (attached) which is a wet tissue product. The front main side (about 14cm x 7 cm) is the waves and the brand name Zelfo. However, in this main side, it should contain more words, which are "Khan uot" (mean wet wipe), and the words "Mat lanh" (mean cooling) and "Tinh khiet" (mean purity). "Khan uot" to indicate function of the product, while Mat lanh and Tinh khiet are just marketing term to add.
So yes, the task is quite simple, but I think the key is to choose an appropriate font, color and the location you decide where it should be. You can add any element you want, as long as it look good overall, and those words above, are required to have. More in the attached are few rival from our market, as some example.
Thank you, and wait your idea.

Hi guys, Just to tell you that the main front design will not change. So the waves and the brand name still keep the same. Just adding more words or elements to it. Thank you guys.

```html
<!DOCTYPE html>
<html lang="vi">
<head>
<meta charset="utf-8">
<title>Zelfo – Khăn ướt dieline</title>
<link href="https://fonts.googleapis.com/css2?family=Arimo:wght@400&family=Bree+Serif&family=Quicksand:wght@500;600;700&display=swap" rel="stylesheet">
<style>
  :root {
    --paper: #ffffff;
    --ink: #111111;
    --brand-blue: #1a9ad6;
    --deep-blue: #1479c4;
    --sky-blue: #8fd3f0;
    --pale-blue: #cdebf8;
    --ribbon-green: #2bb26a;
    --white: #ffffff;
  }
  * { margin: 0; padding: 0; box-sizing: border-box; }
  html, body { width: 848px; height: 1200px; overflow: hidden; background: var(--paper); }
  .canvas { position: relative; width: 848px; height: 1200px; font-family: "Quicksand", sans-serif; }
  .abs { position: absolute; }

  .dim { font-family: "Arimo", sans-serif; color: var(--ink); line-height: 1; white-space: nowrap; }
  .dim-top { font-size: 24px; top: 230px; transform: translateX(-50%); }
  .dim-main { font-size: 28px; }
  .dim-side { font-size: 17px; left: 744px; transform: translate(-50%, -50%) rotate(90deg); }
  .dim-height { font-size: 24px; left: 84px; top: 598px; transform: translate(-50%, -50%) rotate(-90deg); }
  .dim-width { font-size: 28px; left: 420px; top: 940px; transform: translate(-50%, -50%); }

  .wave-art { left: 98px; top: 447px; width: 634px; height: 416px;
    background: linear-gradient(180deg, rgba(255,255,255,0) 0%, rgba(255,255,255,0) 14%, #d7eef9 30%, #8ccbed 45%, #3aa3dc 60%, #1a8bd0 75%, #0f7dc8 100%); }

  .info-text { font-size: 7.5px; color: var(--brand-blue); line-height: 1.15; font-weight: 500; }
  .flip { transform: rotate(180deg); text-align: center; }

  .pill { left: 172px; top: 471px; width: 68px; height: 25px; border-radius: 13px; background: var(--brand-blue);
    color: var(--white); font-weight: 600; font-size: 13px; display: flex; align-items: center; justify-content: center;
    box-shadow: 0 1px 3px rgba(0,0,0,.15); }

  .ribbon { left: 601px; top: 443px; width: 44px; height: 75px; }
  .ribbon-text { left: 601px; top: 465px; width: 44px; text-align: center; color: var(--white); font-weight: 700; line-height: 1; }
  .ribbon-text .k { font-size: 8px; letter-spacing: 1.5px; display: block; }
  .ribbon-text .p { font-size: 12px; display: block; margin-top: 2px; }
  .ribbon-text .b { font-size: 5px; letter-spacing: 1px; display: block; margin-top: 2px; }

  .category { left: 329px; top: 512px; font-family: "Bree Serif", serif; font-size: 30px; color: var(--sky-blue); line-height: 1; }
  .brand-name { left: 300px; top: 528px; width: 240px; text-align: center; font-weight: 700; font-size: 78px; color: var(--brand-blue); line-height: 1; letter-spacing: 1px; }

  .tagline-bar { left: 296px; top: 613px; width: 240px; height: 27px; }
  .tagline { left: 296px; top: 613px; width: 240px; height: 27px; color: var(--white); font-size: 19px; font-weight: 500;
    display: flex; align-items: center; justify-content: center; letter-spacing: .3px; }

  .claim { top: 676px; display: flex; align-items: center; gap: 5px; color: var(--white); font-size: 15px; font-weight: 500; }
  .claim svg { width: 21px; height: 21px; }

  .code-box { left: 508px; top: 751px; width: 150px; height: 59px; background: var(--white); }
  .bh-tab { left: 98px; top: 873px; width: 20px; height: 39px; background: var(--brand-blue); }
  .bh-label { left: 98px; top: 876px; font-size: 8px; font-family: "Arimo", sans-serif; color: var(--ink); transform: rotate(90deg); transform-origin: left top; margin-left: 11px; }
</style>
</head>
<body>
<div class="canvas">

  <div class="abs wave-art" role="img" aria-label="Watercolour layers of blue waves rising from light sky blue to deep ocean blue"></div>

  <svg class="abs" style="left:0;top:0" width="848" height="1200" aria-hidden="true">
    <g fill="#e3f4fc">
      <path d="M190 570h8v-8h7v8h8v7h-8v8h-7v-8h-8z" opacity=".8"/>
      <path d="M186 777h9v-9h8v9h9v8h-9v9h-8v-9h-9z" opacity=".7"/>
      <path d="M214 756h4v-4h4v4h4v4h-4v4h-4v-4h-4z" opacity=".7"/>
      <path d="M591 639h6v-6h5v6h6v5h-6v6h-5v-6h-6z"/>
      <path d="M626 691h4v-4h3v4h4v3h-4v4h-3v-4h-4z"/>
    </g>
    <g fill="#bfe6f7">
      <path d="M323 463h4v-4h3v4h4v3h-4v4h-3v-4h-4z"/>
      <path d="M490 467h4v-4h3v4h4v3h-4v4h-3v-4h-4z"/>
      <path d="M558 510h4v-4h3v4h4v3h-4v4h-3v-4h-4z"/>
      <path d="M638 586h4v-4h3v4h4v3h-4v4h-3v-4h-4z"/>
    </g>
    <path d="M598 551h6v-6h6v6h6v6h-6v6h-6v-6h-6z" fill="none" stroke="#d3ecf8" stroke-width="1.5"/>
    <path d="M206 620h4v-4h4v4h4v4h-4v4h-4v-4h-4z" fill="none" stroke="#e3f4fc" stroke-width="1.2"/>

    <path d="M602 443h43v75l-21.5-12-21.5 12z" fill="var(--ribbon-green)"/>
    <path d="M605 443v68l18.5-10 18.5 10v-68" fill="none" stroke="#ffffff" stroke-width=".8"/>

    <path d="M298 617l4-4h228l4 4v19l-4 4h-228l-4-4z" fill="#9fd5f1" fill-opacity=".85" stroke="#ffffff" stroke-width="1"/>

    <path d="M583 355l28-6 28 6 3 8-6 48-25 6-25-6-6-48z" fill="var(--brand-blue)" role="img" aria-label="Certificate seal"/>

    <g fill="none" stroke="var(--brand-blue)" stroke-width="1.1">
      <rect x="254" y="362" width="22" height="22" rx="3"/>
      <rect x="282" y="362" width="22" height="22" rx="3"/>
      <rect x="310" y="362" width="22" height="22" rx="3"/>
      <rect x="254" y="390" width="22" height="22" rx="3"/>
      <rect x="282" y="390" width="22" height="22" rx="3"/>
      <rect x="310" y="390" width="22" height="22" rx="3"/>
      <rect x="211" y="387" width="22" height="22" rx="3"/>
    </g>
    <g fill="var(--brand-blue)">
      <rect x="259" y="367" width="12" height="12" rx="2" opacity=".55"/>
      <circle cx="293" cy="373" r="6" opacity=".55"/>
      <rect x="315" y="367" width="12" height="12" rx="2" opacity=".55"/>
      <rect x="259" y="395" width="12" height="12" rx="2" opacity=".55"/>
      <circle cx="293" cy="401" r="6" opacity=".55"/>
      <rect x="315" y="395" width="12" height="12" rx="2" opacity=".55"/>
      <rect x="216" y="392" width="12" height="12" rx="2" opacity=".55"/>
    </g>

    <g fill="none" stroke="var(--ink)" stroke-width="1.2" stroke-dasharray="14 7">
      <rect x="98" y="259" width="634" height="653"/>
      <line x1="147" y1="259" x2="147" y2="912"/>
      <line x1="683" y1="259" x2="683" y2="912"/>
      <line x1="98" y1="308" x2="732" y2="308"/>
      <line x1="98" y1="447" x2="732" y2="447"/>
      <line x1="98" y1="724" x2="732" y2="724"/>
      <line x1="98" y1="863" x2="732" y2="863"/>
    </g>
  </svg>

  <div class="abs dim dim-top" style="left:128px">12.5</div>
  <div class="abs dim dim-top dim-main" style="left:414px;top:226px">135</div>
  <div class="abs dim dim-top" style="left:708px">12.5</div>
  <div class="abs dim dim-side" style="top:275px">12.5</div>
  <div class="abs dim dim-side" style="top:359px">35</div>
  <div class="abs dim dim-side" style="top:565px">70</div>
  <div class="abs dim dim-side" style="top:777px">35</div>
  <div class="abs dim dim-side" style="top:890px">12.5</div>
  <div class="abs dim dim-height">165mm</div>
  <div class="abs dim dim-width">160 mm</div>

  <div class="abs info-text" style="left:325px;top:343px">NSX: 2 năm trước HSD<br>HSD: In trên bao bì</div>
  <div class="abs info-text flip" style="left:197px;top:366px;font-size:6px">NƠI QUY ĐỊNH<br>XIN BỎ VÀO ĐÚNG</div>

  <div class="abs pill">1 sheet</div>

  <div class="abs ribbon-text"><span class="k">KILLS</span><span class="p">99.9%</span><span class="b">BACTERIA</span></div>

  <div class="abs category">Khăn ướt</div>
  <div class="abs brand-name">Zelfo</div>
  <div class="abs tagline">Sanitizer Wet Wipes</div>

  <div class="abs claim" style="left:295px">
    <svg viewBox="0 0 20 20" aria-hidden="true"><circle cx="10" cy="10" r="9" fill="none" stroke="#fff" stroke-width="1.4"/><circle cx="10" cy="10" r="6.5" fill="#fff"/><path d="M10 5v10M5.7 7.5l8.6 5M5.7 12.5l8.6-5" stroke="var(--brand-blue)" stroke-width="1.2"/></svg>
    <span>Mát Lạnh</span>
  </div>
  <div class="abs claim" style="left:437px">
    <svg viewBox="0 0 20 20" aria-hidden="true"><circle cx="10" cy="10" r="9" fill="none" stroke="#fff" stroke-width="1.4"/><circle cx="10" cy="10" r="6.5" fill="#fff"/><path d="M6 8c2 0 4 2 4 6 0-4 2-6 4-6-1 3-2 5-4 6-2-1-3-3-4-6z" fill="var(--brand-blue)"/></svg>
    <span>Tinh Khiết</span>
  </div>

  <div class="abs code-box"></div>

  <div class="abs bh-tab"></div>
  <div class="abs bh-label">BH</div>
</div>
</body>
</html>
```